Biz Card for Harrowfield Property Partners - HWPP

Harrowfield Property Partners is a commercial real estate acquisitions firm. We buy commercial property and need to raise capital from investors for each deal we buy. The vibe needs to be: give us your money, we will multiply it.
Our website: www.hrwpp-example.com
Competitors are: https://velmarholdings-example.com/, https://tribanquepartners-example.com/, http://www.ostrellecapital-example.com/
Target Market(s)
High Net Worth Individuals, Bankers, Insurance Companies, Commercial Real Estate Brokers.
Industry/Entity Type
Investment Banking
Contact Information for Business Card
Name, Title, Addess, Cell#, Office#, email, website
Requirements
Must have
- use one of our logos. See website for look and feel: www.hrwpp-example.com
Nice to have
- see website: www.hrwpp-example.com

```html
<!DOCTYPE html>
<html lang="en">
<head>
<meta charset="utf-8">
<title>Harrowfield Property Partners – Business Card</title>
<link rel="stylesheet" href="https://fonts.googleapis.com/css2?family=Lato:wght@300;400&family=Montserrat:wght@600&family=Raleway:wght@400;500&family=Roboto:wght@500&display=swap">
<style>
  :root {
    --backdrop: #e4e4e4;
    --paper: #f7f7f7;
    --navy: #0b3049;
    --navy-deep: #00213a;
    --navy-top: #00304a;
    --navy-bottom: #00253f;
    --ink-grey: #555a5f;
    --white: #ffffff;
  }
  * { box-sizing: border-box; margin: 0; padding: 0; }
  html, body { width: 1200px; height: 1200px; overflow: hidden; }
  body { background: var(--backdrop); position: relative; }

  .card {
    position: absolute;
    left: 262px;
    width: 686px;
    height: 392px;
    border-radius: 19px;
    overflow: hidden;
  }
  .card--front { top: 165px; background: var(--paper); }
  .card--back { top: 653px; background: linear-gradient(180deg, var(--navy-top), var(--navy-bottom)); }

  .brand-mark { position: absolute; border-radius: 50%; }
  .brand-name {
    position: absolute;
    font-family: 'Lato', sans-serif;
    font-weight: 300;
    white-space: nowrap;
    text-transform: uppercase;
  }
  .brand-name span { display: block; }

  .card--front .brand-mark { left: 149px; top: 95px; width: 98px; height: 98px; background: var(--navy); }
  .card--front .brand-name { left: 84px; top: 205px; width: 236px; text-align: center; color: var(--navy); }
  .card--front .brand-name .brand-line1 { font-size: 26px; letter-spacing: 3px; }
  .card--front .brand-name .brand-line2 { font-size: 13px; letter-spacing: 3px; margin-top: 6px; }

  .divider { position: absolute; left: 348px; top: 92px; width: 1.5px; height: 172px; background: var(--navy); }

  .contact { position: absolute; left: 381px; top: 96px; font-family: 'Raleway', sans-serif; color: var(--ink-grey); }
  .contact-name { font-family: 'Montserrat', sans-serif; font-weight: 600; font-size: 21px; color: var(--navy); letter-spacing: 0.2px; }
  .contact-title { font-size: 15px; font-weight: 500; margin-top: 1px; }
  .contact-address { font-size: 15px; line-height: 19px; margin-top: 14px; }
  .contact-list { list-style: none; margin-top: 8px; font-size: 15px; line-height: 20px; }
  .contact-list li { display: flex; align-items: center; gap: 9px; }
  .contact-list svg { width: 12px; height: 12px; fill: var(--navy); flex: none; }

  .web-band {
    position: absolute; left: 0; top: 332px; width: 100%; height: 34px;
    background: var(--navy-deep);
    display: flex; align-items: center; justify-content: center;
  }
  .website { font-family: 'Roboto', sans-serif; font-weight: 500; font-size: 14px; letter-spacing: 5px; color: var(--white); }

  .card--back .brand-mark { left: 120px; top: 137px; width: 118px; height: 118px; background: var(--white); }
  .card--back .brand-name { left: 261px; top: 152px; color: var(--white); }
  .card--back .brand-name .brand-line1 { font-size: 33px; letter-spacing: 4px; }
  .card--back .brand-name .brand-line2 { font-size: 17px; letter-spacing: 4px; margin-top: 8px; }
  .card--back .website { position: absolute; top: 311px; left: 0; width: 100%; text-align: center; }
</style>
</head>
<body>

<section class="card card--front">
  <div class="brand-mark"></div>
  <div class="brand-name">
    <span class="brand-line1">Harrowfield</span>
    <span class="brand-line2">Property Partners</span>
  </div>
  <div class="divider"></div>
  <div class="contact">
    <div class="contact-name">DANIEL WHITCOMBE</div>
    <div class="contact-title">President</div>
    <div class="contact-address">415 Larkspur Ave, Suite 820<br>Fairhaven, FL 33990</div>
    <ul class="contact-list">
      <li><svg viewBox="0 0 24 24"><path d="M6.6 10.8a15.1 15.1 0 0 0 6.6 6.6l2.2-2.2a1 1 0 0 1 1-.25 11.4 11.4 0 0 0 3.6.57 1 1 0 0 1 1 1V20a1 1 0 0 1-1 1A17 17 0 0 1 3 4a1 1 0 0 1 1-1h3.5a1 1 0 0 1 1 1c0 1.25.2 2.45.57 3.57a1 1 0 0 1-.25 1z"/></svg>(555) 014-2285</li>
      <li><svg viewBox="0 0 24 24"><path d="M7 1h10a2 2 0 0 1 2 2v18a2 2 0 0 1-2 2H7a2 2 0 0 1-2-2V3a2 2 0 0 1 2-2zm0 3v14h10V4z"/></svg>(555) 017-6630</li>
      <li><svg viewBox="0 0 24 24"><path d="M2 6h20v12H2zm2 1.5v.6l8 5 8-5v-.6z"/></svg>info@hrwpp-example.com</li>
    </ul>
  </div>
  <div class="web-band"><span class="website">www.hrwpp-example.com</span></div>
</section>

<section class="card card--back">
  <div class="brand-mark"></div>
  <div class="brand-name">
    <span class="brand-line1">Harrowfield</span>
    <span class="brand-line2">Property Partners</span>
  </div>
  <div class="website">www.hrwpp-example.com</div>
</section>

</body>
</html>
```